Brindle Advisory Business Card Design

Business card for business consulting company, using attached logo. We do financial and strategic consulting, and want a clean, professional image with a bit of fun. Our logo is a flat whale tail, which symbolizes the Orca whale, a highly collaborative, group based animal that is very successful in navigating the ocean, protecting the herd, and hunting. We like the logo that is blue and gray on white one one side, but would be open to a blue card with white lettering on the other side... or whatever you'd suggest
Updates
Hi all - I have had the logo modified to take the shadowing off the tail. I will post it on the brief... under a file name called updated logo. thank you Added Saturday, April 25, 2015
Target Market(s)
Small to medium sized businesses ($10M to $500M in revenue per year), financial and sales executives, general managers, attorneys and CPAs
Industry/Entity Type
Financial
Contact Information for Business Card
Want company name, contact info - name, title, telephone, email, website, linkedin, twitter and Facebook. No physical address yet.
Requirements
Must have
- contemporary design, bold, strong, confident but with a bit of fun. prominently feature the logo and the whale tail icon
Nice to have
- unique touches that would differentiate us from a regular card... for example, logo and writing all on front on white background, but on back - logo in white on a blue background
- open to idea of different shapes of card than standard... but not sure
Should not have
- ?

```html
<!DOCTYPE html>
<html lang="en">
<head>
<meta charset="utf-8">
<title>Brindle Advisory – Business Card</title>
<link href="https://fonts.googleapis.com/css2?family=Quicksand:wght@500&family=Montserrat:wght@500;600&family=Open+Sans:wght@400&display=swap" rel="stylesheet">
<style>
  :root{
    --navy:#173e78;
    --navy-deep:#12315f;
    --swoosh:#c9cdd3;
    --ink:#6f757d;
    --paper:#ffffff;
    --paper-shade:#f1f2f4;
    --backdrop:#e4e6e9;
  }
  *{box-sizing:border-box;margin:0;padding:0}
  html,body{width:1200px;height:900px;overflow:hidden}
  body{
    background:var(--backdrop);
    display:flex;flex-direction:column;align-items:center;justify-content:center;gap:40px;
    font-family:"Open Sans",sans-serif;
  }
  .card{
    position:relative;width:700px;height:400px;border-radius:28px;overflow:hidden;
    background:linear-gradient(160deg,var(--paper) 40%,var(--paper-shade));
    box-shadow:0 6px 18px rgba(0,0,0,.12);
  }
  .card__bands{position:absolute;inset:0;width:100%;height:100%}
  .holder{
    position:absolute;top:44px;right:44px;text-align:right;color:var(--paper);
    font-family:"Montserrat",sans-serif;white-space:nowrap;
  }
  .holder__name{font-size:21px;font-weight:600;letter-spacing:2px;text-transform:uppercase}
  .holder__title{font-size:15px;font-weight:500;letter-spacing:1px;margin-top:4px}
  .contacts{position:absolute;left:38px;top:142px;list-style:none}
  .contacts li{display:flex;align-items:center;gap:10px;height:27px;font-size:14px;color:var(--ink);letter-spacing:.4px;white-space:nowrap}
  .contacts svg{width:17px;height:17px;flex:none}
  .brand{display:flex;flex-direction:column;align-items:flex-end;white-space:nowrap}
  .brand__mark{width:56px;height:56px;border-radius:9px;background:var(--navy)}
  .brand__name{
    font-family:"Quicksand",sans-serif;font-weight:500;color:var(--navy);
    font-size:42px;line-height:1;letter-spacing:-.5px;margin-top:8px;
  }
  .brand__tag{font-family:"Open Sans",sans-serif;font-size:12px;color:var(--ink);letter-spacing:1px;margin-top:4px}
  .card--front .brand{position:absolute;right:70px;top:212px}
  .card--back{display:flex;align-items:center;justify-content:center}
  .card--back .brand__name{font-size:48px}
</style>
</head>
<body>

<section class="card card--front" aria-label="Business card front">
  <svg class="card__bands" viewBox="0 0 700 400" preserveAspectRatio="none" aria-hidden="true">
    <path d="M95,0 C330,52 520,112 700,178 V128 C560,82 380,40 150,0 Z" fill="var(--swoosh)"/>
    <path d="M150,0 H700 V128 C560,82 380,40 150,0 Z" fill="var(--navy)"/>
  </svg>

  <div class="holder">
    <p class="holder__name">Daniel Whitmore</p>
    <p class="holder__title">Managing Director</p>
  </div>

  <ul class="contacts">
    <li>
      <svg viewBox="0 0 20 20"><circle cx="10" cy="10" r="10" fill="var(--navy)"/><path d="M7 5.5l1.6 2.3-1 1.2c.6 1.2 1.5 2.1 2.7 2.7l1.2-1 2.3 1.6-.8 1.7c-3.5-.3-6.8-3.6-7.1-7.1z" fill="#fff"/></svg>
      014 555 0192
    </li>
    <li>
      <svg viewBox="0 0 20 20"><circle cx="10" cy="10" r="10" fill="var(--navy)"/><rect x="7" y="4.5" width="6" height="11" rx="1.2" fill="#fff"/><rect x="8" y="6" width="4" height="6.5" fill="var(--navy)"/></svg>
      014 555 0193
    </li>
    <li>
      <svg viewBox="0 0 20 20"><circle cx="10" cy="10" r="10" fill="var(--navy)"/><rect x="5" y="6.5" width="10" height="7" rx="1" fill="#fff"/><path d="M5.4 7l4.6 3.6L14.6 7" fill="none" stroke="var(--navy)" stroke-width="1"/></svg>
      daniel@brindleadvisory.com
    </li>
    <li>
      <svg viewBox="0 0 20 20"><circle cx="10" cy="10" r="10" fill="var(--navy)"/><circle cx="10" cy="10" r="5" fill="none" stroke="#fff" stroke-width="1.2"/><path d="M5 10h10M10 5c-2 2.8-2 7.2 0 10M10 5c2 2.8 2 7.2 0 10" fill="none" stroke="#fff" stroke-width="1"/></svg>
      www.brindleadvisory.com
    </li>
    <li>
      <svg viewBox="0 0 20 20"><circle cx="10" cy="10" r="10" fill="var(--navy)"/><path d="M10 4.5a3.6 3.6 0 0 0-3.6 3.6c0 2.7 3.6 7 3.6 7s3.6-4.3 3.6-7A3.6 3.6 0 0 0 10 4.5z" fill="#fff"/><circle cx="10" cy="8.2" r="1.3" fill="var(--navy)"/></svg>
      42 Harbour Lane, Suite 5
    </li>
  </ul>

  <div class="brand">
    <span class="brand__mark" aria-hidden="true"></span>
    <p class="brand__name">Brindle Advisory</p>
    <p class="brand__tag">business consulting</p>
  </div>
</section>

<section class="card card--back" aria-label="Business card back">
  <div class="brand">
    <span class="brand__mark" aria-hidden="true"></span>
    <p class="brand__name">Brindle Advisory</p>
    <p class="brand__tag">business consulting</p>
  </div>
</section>

</body>
</html>
```